Run Far Ahead Training Web Design and Launch!

A recently new business in Personal Coaching (Fitness) looking to have a professional website built along with using Zentrix system for payments. Ability to set up memberships would be great. Current site is www.rfatrain.example . I used that site to quickly put something together so that I could get started. Also looking to do something similar to www.morvelgym.example with a shop as well as challenges and leaderboards that members and non members alike can participate in. Would like to have a "meet the coaches" page option along with what I currently have on the site.

Target Market(s)

Men and Women 24-60 years old. Weight loss clients

Industry/Entity Type

Fitness

Coding

Coded - Design and coding required

Number of Pages Required

5+ page

Font styles to use
Sans Serif

Colors
33a6d7
f78f20
0255a3
0592cd

Requirements
Must have
• Zentrix or Payment integration. Photo gallery. Reviews page. Calender link for events. Donation location for Stride4AllKO
Nice to have
• Would like to have a page dedicated to challenges/leaderboards. A way for members and non members to input their results of a posted challenge. Like to have similar pages that my current site www.rfatrain.example has. Ways to sign up for a membership. Meet the coaches and athletes. Gallery designed to call out award winning performances (podium or series wins), Meet the coaches and athletes.

```html
<!DOCTYPE html>
<html lang="en">
<head>
<meta charset="utf-8">
<title>Run Far Ahead Training</title>
<link href="https://fonts.googleapis.com/css2?family=Rajdhani:wght@600;700&family=Roboto:wght@400;500;700&display=swap" rel="stylesheet">
<style>
:root{
  --navy:#0255a3;
  --deep:#0d4aa0;
  --blue:#0592cd;
  --sky:#33a6d7;
  --orange:#f78f20;
  --text:#555b63;
  --muted:#777d85;
  --line:#d9dde2;
  --white:#ffffff;
}
*{margin:0;padding:0;box-sizing:border-box}
html,body{width:1200px;height:4431px;overflow:hidden;background:var(--white)}
body{position:relative;font-family:"Roboto",sans-serif;color:var(--text)}
.abs{position:absolute}
.heading{font-family:"Rajdhani",sans-serif;font-weight:700;letter-spacing:1px;color:var(--deep);text-transform:uppercase}
.center{text-align:center}
.photo{position:absolute}

/* header */
.site-header{position:absolute;left:0;top:0;width:1200px;height:108px;background:var(--white)}
.brand{position:absolute;left:75px;top:14px;display:flex;align-items:center;gap:10px}
.brand-dot{width:78px;height:78px;border-radius:50%;background:var(--navy)}
.brand-name{font-family:"Rajdhani",sans-serif;font-weight:700;font-size:28px;color:var(--navy);letter-spacing:.5px}
.nav{position:absolute;top:40px;left:411px;display:flex;gap:0;font-size:14px;font-weight:500;color:#333}
.nav a{position:absolute;white-space:nowrap;text-decoration:none;color:#2b2f35;top:0}
.nav a.active{color:var(--blue)}
.btn-member{position:absolute;left:1035px;top:31px;width:133px;height:38px;background:var(--blue);color:#fff;font-size:13px;font-weight:500;display:flex;align-items:center;justify-content:center;letter-spacing:.3px}

/* hero */
.hero{position:absolute;left:0;top:108px;width:1200px;height:707px;overflow:hidden;
  background:linear-gradient(100deg,#2f6fb3 0%,#5d7d92 30%,#8f8a84 50%,#b9b7b0 70%,#6c8f5c 100%)}
.hero-badge{position:absolute;left:124px;top:102px;width:406px;height:406px;border-radius:50%;
  background:rgba(5,146,205,.88);box-shadow:0 0 0 14px rgba(51,166,215,.35);text-align:center;color:#fff}
.hero-title{font-family:"Rajdhani",sans-serif;font-weight:700;font-size:48px;line-height:50px;letter-spacing:2px;margin-top:110px}
.hero-sub{font-family:"Rajdhani",sans-serif;font-weight:700;font-size:21px;letter-spacing:1px;margin-top:6px}
.btn-orange{display:inline-flex;align-items:center;justify-content:center;background:var(--orange);color:#fff;font-family:"Rajdhani",sans-serif;font-weight:700;font-size:18px;border-radius:30px;letter-spacing:.5px}
.hero-badge .btn-orange{width:195px;height:48px;margin-top:22px}
.arrow{position:absolute;width:30px;height:40px}

/* who we are */
.feature-title{font-family:"Rajdhani",sans-serif;font-weight:700;font-size:18px;line-height:24px;letter-spacing:.3px}
.feature-text{font-size:12.5px;line-height:19px;color:var(--muted)}
.icon-circle{position:absolute;border-radius:50%;display:flex;align-items:center;justify-content:center}

/* coaches */
.coaches{position:absolute;left:0;top:1405px;width:1200px;height:523px;
  background:linear-gradient(180deg,#9cc4e6 0%,#7da6c9 45%,#4d5a7a 80%,#3a3f55 100%)}
.coach-badge{position:absolute;left:652px;top:37px;width:406px;height:406px;border-radius:50%;background:rgba(5,146,205,.9);box-shadow:0 0 0 12px rgba(51,166,215,.4);text-align:center;color:#fff}
.btn-outline{display:inline-flex;align-items:center;justify-content:center;width:175px;height:48px;border:2px solid #fff;border-radius:30px;font-size:14px;font-weight:700;color:#fff}

/* gallery */
.gallery{position:absolute;left:79px;top:2056px;width:1044px;display:grid;grid-template-columns:repeat(4,255px);grid-auto-rows:230px;gap:11px 8px}
.gallery div{width:100%;height:100%}

/* reviews */
.reviews{position:absolute;left:0;top:2562px;width:1200px;height:565px;background:linear-gradient(180deg,#f27f1b,#f78f20)}
.quote{position:absolute;left:473px;top:2780px;width:500px;font-size:19px;line-height:27px;color:#fff}

/* calendar */
.calendar{position:absolute;left:110px;top:3190px;width:437px;height:345px;border:1px solid var(--line);box-shadow:0 2px 4px rgba(0,0,0,.12);background:#fff}
.cal-head{height:56px;background:var(--navy);display:flex;align-items:center;color:#fff;font-size:24px}
.cal-head span.nav-cell{width:56px;height:56px;display:flex;align-items:center;justify-content:center}
.cal-head .month{flex:1;text-align:center;border-left:1px solid rgba(255,255,255,.4);border-right:1px solid rgba(255,255,255,.4);height:56px;line-height:56px}
.cal-grid{display:grid;grid-template-columns:repeat(7,57px);justify-content:center;padding:0 12px}
.cal-days{margin-top:14px}
.cal-days span{display:flex;align-items:center;justify-content:center;height:26px;margin:0 6px;background:var(--navy);color:#fff;font-size:13px;border:1px solid #8fb0d6}
.cal-dates{margin-top:18px;row-gap:9px}
.cal-dates span{display:flex;align-items:center;justify-content:center;height:26px;margin:0 13px;font-size:15px;color:#333}
.cal-dates span.off{color:#aaa}
.cal-dates span.on{background:var(--navy);color:#fff}
.event{position:absolute;left:612px;width:440px;height:110px;display:flex;align-items:center}
.event-pic{width:96px;height:96px;border-radius:50%;flex:none;margin-left:12px}
.event-body{margin-left:20px}
.event-title{font-size:14px;font-weight:700;color:var(--navy)}
.event-text{font-size:13px;line-height:22px;color:var(--muted);margin-top:6px}

/* newsletter + footer */
.lower{position:absolute;left:0;top:3627px;width:1200px;height:804px;background:linear-gradient(100deg,#0a4aa2 0%,#1466b8 45%,#2a92d6 100%)}
.signup{position:absolute;left:299px;top:186px;width:591px;height:56px;border-radius:30px;background:#fff;border:3px solid #3f78c0}
.signup .email{position:absolute;left:28px;top:16px;font-size:17px;color:#333}
.signup .btn-orange{position:absolute;right:6px;top:5px;width:168px;height:42px;font-family:"Roboto",sans-serif;font-size:16px}
.foot-h{position:absolute;font-size:19px;color:#fff;letter-spacing:1px;font-weight:500}
.contact-row{position:absolute;left:363px;display:flex;align-items:center;gap:20px;color:#fff;font-size:16px}
.contact-row i{width:46px;height:46px;border-radius:50%;background:#fff;display:flex;align-items:center;justify-content:center}
.insta{position:absolute;left:839px;top:4135px;display:grid;grid-template-columns:repeat(3,73px);grid-auto-rows:60px;gap:8px 8px}
.social{position:absolute;top:4253px;width:30px;height:30px;border-radius:50%;border:2px solid #fff}
</style>
</head>
<body>

<header class="site-header">
  <div class="brand"><span class="brand-dot"></span><span class="brand-name">RUN FAR AHEAD</span></div>
  <nav class="nav">
    <a class="active" style="left:0">CHALLENGES</a>
    <a style="left:124px">SHOP</a>
    <a style="left:195px">MEET THE COACHES</a>
    <a style="left:368px">CONTACT</a>
    <a style="left:467px">BLOG</a>
    <a style="left:534px">ATHLETE</a>
  </nav>
  <div class="btn-member">MEMBERSHIP</div>
</header>

<section class="hero" role="img" aria-label="Coach guiding a woman doing push-ups in a gym">
  <div class="hero-badge">
    <div class="hero-title">COACHES<br>WHO CARE</div>
    <div class="hero-sub">LET'S WORK OUT TOGETHER!</div>
    <div class="btn-orange">DONATE NOW</div>
  </div>
  <svg class="arrow" style="left:40px;top:255px" viewBox="0 0 30 40"><path d="M22 4 L8 20 L22 36" fill="none" stroke="#fff" stroke-width="4"/></svg>
  <svg class="arrow" style="left:1130px;top:255px" viewBox="0 0 30 40"><path d="M8 4 L22 20 L8 36" fill="none" stroke="#fff" stroke-width="4"/></svg>
</section>
<svg class="abs" style="left:0;top:700px" width="1200" height="116" viewBox="0 0 1200 116">
  <path d="M0 116 L0 110 Q600 -95 1200 84 L1200 116 Z" fill="#fff"/>
  <path d="M120 78 Q600 -62 1110 74" fill="none" stroke="#f78f20" stroke-width="4"/>
</svg>

<h2 class="heading abs center" style="left:0;top:772px;width:1200px;font-size:36px">WHO WE ARE</h2>
<p class="abs center" style="left:320px;top:822px;width:560px;font-size:16.5px;line-height:27px;color:var(--muted)">Augiat in pede Fusce tellus Sed metus augue convallis et vehicula ut pulvinar eu ante Integer orci tellus tristique</p>

<div class="abs" style="left:160px;top:1008px;width:195px;text-align:right">
  <div class="feature-title" style="color:var(--blue)">KNOWLEDGEABLE<br>TRAINING EXPERTISE</div>
  <div class="feature-text" style="margin-top:8px">With years of success and experience, we are capable</div>
</div>
<div class="icon-circle" style="left:371px;top:999px;width:80px;height:80px;background:var(--sky)">
  <svg width="40" height="40" viewBox="0 0 40 40" fill="none" stroke="#fff" stroke-width="2.5"><path d="M20 5a11 11 0 0 0-6 20v5h12v-5a11 11 0 0 0-6-20z"/><path d="M15 34h10"/></svg>
</div>
<div class="photo" role="img" aria-label="Team photo of athletes with medals, framed in a circle" style="left:485px;top:930px;width:230px;height:230px;border-radius:50%;border:4px solid var(--navy);background:radial-gradient(circle,#6b7380,#2c3440)"></div>
<div class="icon-circle" style="left:743px;top:999px;width:80px;height:80px;background:var(--navy)">
  <svg width="44" height="30" viewBox="0 0 44 30" fill="none" stroke="#fff" stroke-width="2.5"><path d="M4 8h26a10 10 0 1 1-10 12H8z"/><circle cx="30" cy="18" r="4"/></svg>
</div>
<div class="abs" style="left:838px;top:1000px;width:230px">
  <div class="feature-title" style="color:var(--navy)">COACHES WHO CARE</div>
  <div class="feature-text" style="margin-top:6px">Our coaches take your fitness goals seriously. We understand that losing weight and gaining muscle</div>
</div>
<div class="icon-circle" style="left:558px;top:1181px;width:80px;height:80px;background:var(--orange)">
  <svg width="44" height="44" viewBox="0 0 44 44" fill="none" stroke="#fff" stroke-width="2.5"><circle cx="22" cy="22" r="16"/><circle cx="22" cy="22" r="10"/><circle cx="22" cy="22" r="4"/><path d="M22 22 L38 6"/></svg>
</div>
<div class="abs center" style="left:460px;top:1272px;width:280px">
  <div class="feature-title" style="color:var(--orange)">YOUR SUCCESS IS OUR GOAL</div>
  <div class="feature-text" style="margin-top:6px">We understand that adapting new fitness habits is difficult and often times fails.</div>
</div>

<section class="coaches" role="img" aria-label="Athletes climbing over an obstacle course frame under a blue sky">
  <div class="coach-badge">
    <div class="heading" style="color:#fff;font-size:34px;margin-top:102px">OUR COACHES</div>
    <p style="font-size:15.5px;line-height:26px;margin:12px 52px 0">Augiat in pede Fusce tellus Sed metus augue convallis et vehicula ut pulvinar eu ante Integer orci tellus tristique vitae consequat nec mauris vive</p>
    <div class="btn-outline" style="margin-top:20px">LEARN MORE</div>
  </div>
</section>

<h2 class="heading abs center" style="left:0;top:1978px;width:1180px;font-size:36px">PHOTO GALLERY</h2>
<div class="gallery">
  <div role="img" aria-label="Group of athletes in a gym" style="background:linear-gradient(#55595f,#2c2f33)"></div>
  <div role="img" aria-label="Team celebrating outdoors under blue sky" style="background:linear-gradient(#3d78c6,#3a3f4a)"></div>
  <div role="img" aria-label="Finishers posing with medals at a race" style="background:linear-gradient(#4b5560,#6a5f72)"></div>
  <div role="img" aria-label="Athlete portrait outdoors" style="background:linear-gradient(#8a9aa6,#33405a)"></div>
  <div role="img" aria-label="Athlete climbing a rope on an obstacle" style="background:linear-gradient(#5b6c8a,#2b2f3a)"></div>
  <div role="img" aria-label="Runner on a blue track" style="background:linear-gradient(#9fc4e8,#3a78c0)"></div>
  <div role="img" aria-label="Athlete running in a stadium" style="background:linear-gradient(#6f8f5a,#7a6252)"></div>
  <div role="img" aria-label="Black and white photo of a racer" style="background:linear-gradient(#9a9a9a,#3a3a3a)"></div>
</div>

<section class="reviews" role="img" aria-label="Faint photo of runners behind an orange overlay"></section>
<svg class="abs" style="left:0;top:2561px" width="1200" height="50" viewBox="0 0 1200 50"><path d="M0 0 L1200 0 L1200 2 Q600 80 0 2 Z" fill="#fff"/></svg>
<h2 class="heading abs center" style="left:0;top:2698px;width:1200px;font-size:36px;color:#fff">REVIEWS</h2>
<div class="photo" role="img" aria-label="Reviewer portrait in a circle" style="left:236px;top:2788px;width:148px;height:148px;border-radius:50%;border:5px solid #fff;background:radial-gradient(circle,#5a5a66,#1e1e24)"></div>
<svg class="abs" style="left:396px;top:2792px" width="58" height="44" viewBox="0 0 58 44" fill="none" stroke="#fde3c6" stroke-width="2.5"><path d="M24 4C10 8 4 18 6 32a8 8 0 1 0 10-8"/><path d="M52 4C38 8 32 18 34 32a8 8 0 1 0 10-8"/></svg>
<p class="quote">If you're looking for a fitness professional that can help you reach your goals in OCR or otherwise, Marcus is top notch. I have been working with him for several months and with his programming and guidance</p>
<div class="abs" style="left:473px;top:2902px;font-size:21px;font-weight:500;color:#fff">Dana Keller</div>
<svg class="abs" style="left:473px;top:2940px" width="122" height="22" viewBox="0 0 122 22" fill="#fff">
  <path id="star" d="M11 1l3 7 7 .5-5.5 4.5 2 7L11 16l-6.5 4 2-7L1 8.5 8 8z"/>
  <use href="#star" x="25"/><use href="#star" x="50"/><use href="#star" x="75"/><use href="#star" x="100"/>
</svg>
<svg class="arrow" style="left:115px;top:2826px;width:24px;height:32px" viewBox="0 0 30 40"><path d="M22 4 L8 20 L22 36" fill="none" stroke="#fff" stroke-width="4"/></svg>
<svg class="arrow" style="left:1063px;top:2826px;width:24px;height:32px" viewBox="0 0 30 40"><path d="M8 4 L22 20 L8 36" fill="none" stroke="#fff" stroke-width="4"/></svg>
<svg class="abs" style="left:0;top:3040px" width="1200" height="88" viewBox="0 0 1200 88"><path d="M0 88 L0 86 Q600 -80 1200 86 L1200 88 Z" fill="#fff"/></svg>

<h2 class="heading abs center" style="left:0;top:3098px;width:1180px;font-size:33px">EVENT CALENDAR</h2>
<div class="calendar">
  <div class="cal-head">
    <span class="nav-cell">&#8592;</span><span class="month">February 2020</span><span class="nav-cell">&#8594;</span>
  </div>
  <div class="cal-grid cal-days"><span>MON</span><span>TUE</span><span>WED</span><span>THU</span><span>FRI</span><span>SAT</span><span>SUN</span></div>
  <div class="cal-grid cal-dates">
    <span class="off">30</span><span class="off">31</span><span>1</span><span>2</span><span>3</span><span>4</span><span>5</span>
    <span>6</span><span>7</span><span>8</span><span>9</span><span>10</span><span class="on">11</span><span>12</span>
    <span>13</span><span>14</span><span class="on">15</span><span>16</span><span>17</span><span>18</span><span>19</span>
    <span>20</span><span>21</span><span>22</span><span>23</span><span>24</span><span>25</span><span>26</span>
    <span>27</span><span class="on">28</span><span>29</span>
  </div>
</div>

<div class="event" style="top:3175px">
  <div class="event-pic" role="img" aria-label="Event photo of a coach at a race" style="background:radial-gradient(circle,#7a8a9a,#2a3040)"></div>
  <div class="event-body"><div class="event-title">EVENT TITLE HERE</div><div class="event-text">Augiat in pede Fusce tellus Sed metus augue<br>convallis et vehicula ut pulvinar</div></div>
</div>
<div class="abs" style="left:612px;top:3298px;width:440px;height:1px;background:var(--line)"></div>
<div class="event" style="top:3304px">
  <div class="event-pic" role="img" aria-label="Event photo of a group workout" style="background:radial-gradient(circle,#8a9fb4,#2e3a4e)"></div>
  <div class="event-body"><div class="event-title">EVENT TITLE HERE</div><div class="event-text">Augiat in pede Fusce tellus Sed metus augue<br>convallis et vehicula ut pulvinar</div></div>
</div>
<div class="abs" style="left:612px;top:3422px;width:440px;height:1px;background:var(--line)"></div>
<div class="event" style="top:3432px">
  <div class="event-pic" role="img" aria-label="Event photo of an athlete on an obstacle" style="background:radial-gradient(circle,#9a7a8a,#2a2a3a)"></div>
  <div class="event-body"><div class="event-title">EVENT TITLE HERE</div><div class="event-text">Augiat in pede Fusce tellus Sed metus augue<br>convallis et vehicula ut pulvinar</div></div>
</div>

<section class="lower">
  <h2 class="heading abs center" style="left:0;top:70px;width:1180px;font-size:36px;color:#fff">NEWSLETTER SIGN UP</h2>
  <p class="abs center" style="left:0;top:124px;width:1180px;font-size:17px;line-height:21px;color:#fff">Sign up to hear from us about specials, sales, and events.<br>As well as health and wellness updates.</p>
  <div class="signup"><span class="email">Email address</span><span class="btn-orange">SUBSCRIBE</span></div>
  <svg class="abs" style="left:0;top:338px" width="1200" height="80" viewBox="0 0 1200 80"><path d="M70 72 Q600 -40 1150 48" fill="none" stroke="#fff" stroke-width="3"/></svg>
</section>

<div class="abs" style="left:140px;top:4090px;width:160px;text-align:center">
  <div style="width:84px;height:84px;border-radius:50%;background:#fff;margin:0 auto"></div>
  <div style="font-family:'Rajdhani',sans-serif;font-weight:700;font-size:20px;line-height:22px;color:#fff;margin-top:10px">RUN FAR AHEAD<br>TRAINING</div>
</div>
<span class="social" style="left:155px"></span>
<span class="social" style="left:199px"></span>
<span class="social" style="left:243px"></span>

<div class="foot-h" style="left:363px;top:4090px">CONTACT US</div>
<div class="contact-row" style="top:4137px"><i><svg width="22" height="22" viewBox="0 0 24 24" fill="#0255a3"><path d="M6.6 10.8a15 15 0 0 0 6.6 6.6l2.2-2.2a1 1 0 0 1 1-.25 11.4 11.4 0 0 0 3.6.57 1 1 0 0 1 1 1V20a1 1 0 0 1-1 1A17 17 0 0 1 3 4a1 1 0 0 1 1-1h3.5a1 1 0 0 1 1 1c0 1.25.2 2.45.57 3.57a1 1 0 0 1-.25 1z"/></svg></i>888-888-8888</div>
<div class="contact-row" style="top:4207px"><i><svg width="20" height="16" viewBox="0 0 20 16" fill="none" stroke="#0255a3" stroke-width="2"><rect x="1" y="1" width="18" height="14"/><path d="M1 1l9 8 9-8"/></svg></i>info@rfatrain.example</div>
<div class="contact-row" style="top:4277px"><i><svg width="18" height="24" viewBox="0 0 18 24" fill="#0255a3"><path d="M9 0a9 9 0 0 0-9 9c0 7 9 15 9 15s9-8 9-15a9 9 0 0 0-9-9zm0 12.5A3.5 3.5 0 1 1 9 5.5a3.5 3.5 0 0 1 0 7z"/></svg></i>Lorem ipsum dolor sit</div>

<div class="foot-h" style="left:641px;top:4090px">PARTNERS</div>
<div class="abs" style="left:646px;top:4152px;width:106px;height:58px;background:#fff;border-radius:4px"></div>

<div class="foot-h" style="left:837px;top:4090px">INSTAGRAM</div>
<div class="insta">
  <div role="img" aria-label="Instagram post: boat on water" style="background:linear-gradient(#c7a46a,#6a5a3a)"></div>
  <div role="img" aria-label="Instagram post: runner on track" style="background:linear-gradient(#9ec3e6,#4a7cb8)"></div>
  <div role="img" aria-label="Instagram post: race crowd" style="background:linear-gradient(#7fa7d8,#5a6a3a)"></div>
  <div role="img" aria-label="Instagram post: athletes at an event" style="background:linear-gradient(#8a6a5a,#3a3a4a)"></div>
  <div role="img" aria-label="Instagram post: products on a table" style="background:linear-gradient(#e7d25a,#5ab0c8)"></div>
  <div role="img" aria-label="Instagram post: group photo" style="background:linear-gradient(#7a4a5a,#2a2a3a)"></div>
</div>
<div class="abs" style="left:841px;top:4296px;font-size:12px;color:#fff;text-decoration:underline;display:flex;align-items:center;gap:6px"><span style="width:11px;height:11px;border:1.5px solid #fff;border-radius:3px;display:inline-block"></span>FOLLOW US INSTAGRAM</div>

<div class="abs" style="left:150px;top:4384px;font-size:14px;color:#fff">Copyrights 2020. All rights reserved</div>

</body>
</html>
```